Talvero Networks LLC
Consultant, Health Care Operations
Talvero Networks LLC -
Creative Brief
Use specific fonts
I like Calibri, Tahoma, Lucida (rounded but professional) but am open to other similar fonts
Simple
Dwight Pennock
President, CEO
PO BOX 418263 Coral Springs, FL 33077
dwight@talverohub.com
talverohub.com

```html
<!DOCTYPE html>
<html lang="en">
<head>
<meta charset="utf-8">
<title>Talvero Networks LLC — Stationery</title>
<link rel="stylesheet" href="https://fonts.googleapis.com/css2?family=Carlito:wght@400;700&display=swap">
<style>
  :root {
    --backdrop: #e6e9ec;
    --paper: #ffffff;
    --brand-blue: #1c95d2;
    --brand-sky: #6cc9ef;
    --brand-navy: #15507f;
    --ink: #262626;
    --ink-soft: #5b5f64;
    --shadow: 0 6px 18px rgba(0,0,0,0.18);
  }
  * { box-sizing: border-box; margin: 0; padding: 0; }
  html, body { width: 1200px; height: 760px; overflow: hidden; }
  body {
    background: var(--backdrop);
    font-family: "Carlito", "Calibri", sans-serif;
    color: var(--ink);
  }
  .canvas { position: relative; width: 1200px; height: 760px; }

  .sheet { position: absolute; background: var(--paper); box-shadow: var(--shadow); overflow: hidden; }
  .swoosh { position: absolute; top: 0; left: 0; width: 100%; display: block; }

  .wordmark { display: flex; align-items: center; gap: 6px; }
  .wordmark-dot { border-radius: 50%; background: var(--brand-blue); flex: none; }
  .wordmark-name { font-weight: 700; color: var(--brand-navy); letter-spacing: 0.02em; line-height: 1; }
  .wordmark-sub { color: var(--ink-soft); letter-spacing: 0.18em; text-transform: uppercase; }

  /* letterhead */
  .letterhead { left: 40px; top: 40px; width: 526px; height: 680px; }
  .letterhead .brand { position: absolute; left: 40px; top: 48px; }
  .letterhead .wordmark-dot { width: 22px; height: 22px; }
  .letterhead .wordmark-name { font-size: 34px; }
  .letterhead .wordmark-sub { font-size: 8px; margin-top: 4px; padding-left: 28px; }
  .letterhead-footer {
    position: absolute; left: 40px; right: 40px; bottom: 28px;
    border-top: 2px solid var(--brand-blue); padding-top: 8px;
    font-size: 8.6px; color: var(--ink);
    display: flex; justify-content: space-between; white-space: nowrap;
  }
  .letterhead-footer .sep { color: var(--brand-blue); }
  .letterhead-footer .label { color: var(--brand-blue); font-weight: 700; }

  /* business cards */
  .card { width: 275px; height: 158px; }
  .card-front-a { left: 600px; top: 40px; }
  .card-back-a  { left: 895px; top: 40px; background: linear-gradient(135deg, var(--brand-sky), var(--brand-blue)); color: var(--paper); }
  .card-back-b  { left: 600px; top: 218px; background: linear-gradient(135deg, var(--brand-blue), var(--brand-sky)); color: var(--paper); }
  .card-front-b { left: 895px; top: 218px; }

  .card-name-band {
    position: absolute; left: 0; top: 0; width: 100%; height: 52px;
    background: linear-gradient(90deg, var(--brand-blue), var(--brand-sky));
    padding: 10px 16px; color: var(--paper);
  }
  .card-name { font-size: 15px; font-weight: 700; line-height: 1.1; }
  .card-title { font-size: 10px; }
  .card-contact { position: absolute; left: 16px; top: 64px; font-size: 9.5px; line-height: 1.45; color: var(--ink); }
  .card-contact .label { color: var(--brand-blue); font-weight: 700; }
  .card-front-a .brand { position: absolute; right: 14px; bottom: 12px; }
  .card .wordmark-dot { width: 9px; height: 9px; }
  .card .wordmark-name { font-size: 14px; }

  .card-tagline { position: absolute; left: 18px; top: 22px; }
  .card-tagline .kicker { font-size: 10px; letter-spacing: 0.04em; }
  .card-tagline .headline { font-size: 22px; font-weight: 700; line-height: 1.05; }
  .card-tagline .sub { font-size: 10px; }
  .card-services { position: absolute; left: 18px; bottom: 18px; font-size: 9px; line-height: 1.45; }
  .card-back-b .brand { position: absolute; right: 16px; bottom: 14px; }
  .card-back-b .wordmark-name { color: var(--paper); }
  .card-back-b .wordmark-dot { background: var(--paper); }

  .card-front-b .card-tagline .headline { color: var(--brand-blue); }
  .card-front-b .card-tagline .kicker, .card-front-b .card-tagline .sub { color: var(--ink-soft); }
  .card-front-b .card-services { color: var(--ink); }
  .card-front-b .brand { position: absolute; right: 16px; bottom: 14px; }
  .card-front-b .wordmark-name { font-size: 20px; }
  .card-front-b .wordmark-dot { width: 12px; height: 12px; }

  /* envelopes */
  .envelope { width: 400px; height: 160px; }
  .envelope-front { left: 600px; top: 398px; }
  .envelope-front .brand { position: absolute; left: 22px; top: 34px; }
  .envelope-front .wordmark-dot { width: 14px; height: 14px; }
  .envelope-front .wordmark-name { font-size: 22px; }
  .envelope-front .wordmark-sub { font-size: 6px; margin-top: 3px; padding-left: 20px; }
  .return-address { position: absolute; left: 22px; top: 84px; font-size: 9px; line-height: 1.4; font-style: normal; }

  .envelope-back { left: 770px; top: 570px; }
  .envelope-back .folds { position: absolute; inset: 0; width: 100%; height: 100%; display: block; }
  .flap-web { position: absolute; left: 0; right: 0; top: 30px; text-align: center; font-size: 10px; color: var(--paper); letter-spacing: 0.03em; }
</style>
</head>
<body>
<main class="canvas">

  <section class="sheet letterhead" aria-label="Letterhead">
    <svg class="swoosh" viewBox="0 0 526 210" height="210" preserveAspectRatio="none" aria-hidden="true">
      <defs>
        <linearGradient id="lh-blue" x1="0" y1="0" x2="1" y2="1">
          <stop offset="0" stop-color="#6cc9ef"/>
          <stop offset="1" stop-color="#1c95d2"/>
        </linearGradient>
      </defs>
      <path d="M170 0 H526 V168 C430 120 300 48 170 0 Z" fill="url(#lh-blue)"/>
      <path d="M140 0 C290 58 420 136 526 196" fill="none" stroke="#111" stroke-width="4"/>
    </svg>
    <div class="brand">
      <div class="wordmark"><span class="wordmark-dot"></span><span class="wordmark-name">TALVERO</span></div>
      <div class="wordmark-sub">Networks LLC</div>
    </div>
    <footer class="letterhead-footer">
      <span>PO BOX 418263 Brookhaven Falls, FL 34990</span><span class="sep">|</span>
      <span><span class="label">P:</span> 555.204.3198</span><span class="sep">|</span>
      <span><span class="label">E:</span> dwight@talverohub.com</span><span class="sep">|</span>
      <span><span class="label">W:</span> www.talverohub.com</span>
    </footer>
  </section>

  <section class="sheet card card-front-a" aria-label="Business card front">
    <div class="card-name-band">
      <div class="card-name">Dwight Pennock</div>
      <div class="card-title">President, CEO</div>
    </div>
    <div class="card-contact">
      <div>PO BOX 418263</div>
      <div>Brookhaven Falls, FL 34990</div>
      <div><span class="label">P:</span> 555.204.3198</div>
      <div><span class="label">E:</span> dwight@talverohub.com</div>
      <div><span class="label">W:</span> talverohub.com</div>
    </div>
    <div class="brand"><div class="wordmark"><span class="wordmark-dot"></span><span class="wordmark-name">TALVERO</span></div></div>
  </section>

  <section class="sheet card card-back-a" aria-label="Business card back">
    <div class="card-tagline">
      <div class="kicker">Consultant</div>
      <div class="headline">Health Care</div>
      <div class="sub">Operations</div>
    </div>
    <div class="card-services">
      <div>Clinical Workflow and Coding</div>
      <div>Staffing and Revenue Support</div>
    </div>
  </section>

  <section class="sheet card card-back-b" aria-label="Business card back, alternate">
    <div class="card-tagline">
      <div class="kicker">Consultant</div>
      <div class="headline">Health Care</div>
      <div class="sub">Operations</div>
    </div>
    <div class="card-services">
      <div>Clinical Workflow and Coding</div>
      <div>Staffing and Revenue Support</div>
    </div>
    <div class="brand"><div class="wordmark"><span class="wordmark-dot"></span><span class="wordmark-name">TALVERO</span></div></div>
  </section>

  <section class="sheet card card-front-b" aria-label="Business card front, alternate">
    <div class="card-tagline">
      <div class="kicker">Consultant</div>
      <div class="headline">Health Care</div>
      <div class="sub">Operations</div>
    </div>
    <div class="card-services">
      <div>Clinical Workflow and Coding</div>
      <div>Staffing and Revenue Support</div>
    </div>
    <div class="brand"><div class="wordmark"><span class="wordmark-dot"></span><span class="wordmark-name">TALVERO</span></div></div>
  </section>

  <section class="sheet envelope envelope-front" aria-label="Envelope front">
    <svg class="swoosh" viewBox="0 0 400 70" height="70" preserveAspectRatio="none" aria-hidden="true">
      <defs>
        <linearGradient id="env-blue" x1="0" y1="0" x2="1" y2="1">
          <stop offset="0" stop-color="#6cc9ef"/>
          <stop offset="1" stop-color="#1c95d2"/>
        </linearGradient>
      </defs>
      <path d="M120 0 H400 V60 C320 40 220 16 120 0 Z" fill="url(#env-blue)"/>
      <path d="M100 0 C220 20 320 44 400 68" fill="none" stroke="#111" stroke-width="3"/>
    </svg>
    <div class="brand">
      <div class="wordmark"><span class="wordmark-dot"></span><span class="wordmark-name">TALVERO</span></div>
      <div class="wordmark-sub">Networks LLC</div>
    </div>
    <address class="return-address">
      <div>PO BOX 418263</div>
      <div>Brookhaven Falls, FL 34990</div>
    </address>
  </section>

  <section class="sheet envelope envelope-back" aria-label="Envelope back">
    <svg class="folds" viewBox="0 0 400 160" preserveAspectRatio="none" aria-hidden="true">
      <defs>
        <linearGradient id="flap-blue" x1="0" y1="0" x2="0" y2="1">
          <stop offset="0" stop-color="#1c95d2"/>
          <stop offset="1" stop-color="#6cc9ef"/>
        </linearGradient>
      </defs>
      <path d="M0 160 L160 70 M400 160 L240 70" stroke="#d6dadd" stroke-width="1.2" fill="none"/>
      <path d="M0 0 H400 L220 92 Q200 102 180 92 Z" fill="url(#flap-blue)"/>
    </svg>
    <div class="flap-web">www.talverohub.com</div>
  </section>

</main>
</body>
</html>
```